Infographic for a Christian church discipleship pathway

We need to take a fairly complex program that helps people in a Baptist church follow Jesus, and turn it into a simple graphic. This graphic does not have to explain the whole program, web pages and print materials will do that. But, it should be something that people see and understand what it is quickly. The attached graphic is only to give the key words and general direction of the program. It should not serve as a design guide. In other words, we want to see some other ideas how this information can be imparted graphically with concision and creativity. It's important to note, the categories at the top (pray daily, read daily, gather weekly) are first steps, starting points....one shouldn't move forward until they've incorporated these things into their life. However, the categories that follow (study, connect, serve, etc) are not necessarily steps to take in sequential order.

The diagrams we've provided are not what we expect. They are only to explain the program. Here is a verbal description: The motto of our church is "A Ready Church" (ready to serve, ready to love, ready for when Jesus returns). There are four words that describe a ready church member: FOCUSED on the return of Christ, FAITHFUL in a daily relationship with Jesus, PREPARED for any opportunity to be a supernatural vessel of God's worK, LOOKING to invite others into God's family. The first two are God's Work in Me (Focused and faithful); the second two are God's Work Through me (Prepared, looking). Please use those two things as you wish (Focused faithful prepared looking; and God's word in and through me). If they are clarifying, please use. If not, you don't have to use.

Additionally, the strategies we employ to be "a ready church" are 1. Prayer 2. God's Word, and 3. Biblical Community. (So, in other words, these three things help us be a people who is focused, faithful, prepared, and looking....which is a ready church.

To provide some information how we will build this out: this graphic will be used in print and digital content. The digital content will allow people to click on each category to access training and resources associated with that discipline. (Fasting, reflecting, etc).

www.qvd.church

Target Market(s)

35-50

Industry/Entity Type

Religious

Other font styles liked:
• Lato and/or Cambria

Requirements
Must have
• Fonts: lato, cambria. Colors#: 373E41, ebebe8, #a69677. Accent Colors: 80401D, #4e5730, #a5bac8
Nice to have
• A designer who has an understanding of what it means to incorporate the spiritual disciplines of the Christian faith into their life.

```html
<!DOCTYPE html>
<html lang="en">
<head>
<meta charset="utf-8">
<title>A Ready Church – Discipleship Pathway</title>
<link href="https://fonts.googleapis.com/css2?family=Poppins:wght@400;500;600;700;800&display=swap" rel="stylesheet">
<style>
  :root{
    --charcoal:#373e41;
    --tan:#a69677;
    --stone:#ebebe8;
    --row-grey:#dcdcdc;
    --white:#ffffff;
    --backdrop:#adadad;
    --chev-mid:#6d7275;
    --chev-light:#b9bbbc;
  }
  *{margin:0;padding:0;box-sizing:border-box}
  html,body{width:1200px;height:1089px;overflow:hidden;background:var(--backdrop);font-family:"Poppins",sans-serif}
  .poster{position:absolute;left:107px;top:164px;width:1232px;height:952px;transform:scale(.8);transform-origin:0 0;
    background:linear-gradient(180deg,#ffffff 0%,#f6f6f5 55%,#ececeb 100%);overflow:hidden}
  .abs{position:absolute}
  .brand{left:41px;top:52px;display:flex;align-items:center;gap:12px}
  .brand-mark{width:30px;height:30px;background:var(--charcoal)}
  .brand-name{font-weight:600;font-size:25px;line-height:26px;color:var(--charcoal);letter-spacing:.5px}
  .title-box{left:342px;top:45px;width:845px;height:150px;border:3px solid var(--charcoal);background:var(--white)}
  .title{position:absolute;left:0;right:0;top:-14px;text-align:center;font-weight:700;font-size:86px;line-height:110px;color:var(--charcoal);letter-spacing:1px}
  .tagline{position:absolute;left:0;right:0;bottom:0;height:60px;background:var(--tan);color:var(--white);
    font-weight:700;font-size:21px;display:flex;align-items:center;justify-content:center}
  .steeple-art{left:158px;top:195px;width:174px;height:285px;background:linear-gradient(180deg,#bdbdbd,#9c9c9c);opacity:.85;border-radius:4px 4px 0 0}
  .pillar{top:283px;height:187px;color:var(--white);text-align:center;padding-top:48px}
  .pillar.dark{background:var(--charcoal)}
  .pillar.tan{background:var(--tan)}
  .p1{left:340px;width:263px;border-top-left-radius:24px}
  .p2{left:623px;width:281px}
  .p3{left:924px;width:264px}
  .pillar h2{font-weight:700;font-size:34px;line-height:34px}
  .pillar h2 .cap{font-size:44px}
  .pillar p{font-size:15px;line-height:19px;margin:6px auto 0;width:180px}
  .pointer{top:365px;width:0;height:0;border-top:10px solid transparent;border-bottom:10px solid transparent}
  .pt1{left:603px;border-left:16px solid var(--charcoal)}
  .pt2{left:904px;border-left:16px solid var(--tan)}
  .badge{width:88px;height:88px;border-radius:50%;background:var(--charcoal);border:4px solid var(--white);
    box-shadow:0 2px 6px rgba(0,0,0,.35);top:238px}
  .badge span{position:absolute;inset:16px;border-radius:50%;background:#5b6265}
  .b1{left:436px}.b2{left:720px}.b3{left:1003px}
  .habit{top:476px;height:44px;color:var(--white);font-weight:700;font-size:23px;display:flex;align-items:center;justify-content:center}
  .habit.dark{background:var(--charcoal)}
  .habit.tan{background:var(--tan)}
  .start{left:46px;top:477px;width:286px;height:42px;background:var(--charcoal);border-top-left-radius:22px;
    color:var(--white);font-weight:700;font-size:18px;letter-spacing:5px;display:flex;align-items:center;padding-left:33px;gap:2px}
  .side{left:46px;top:519px;width:286px;height:353px;background:var(--tan);border-bottom-left-radius:30px;color:var(--white)}
  .side-block{position:absolute;left:20px}
  .side-block strong{display:block;font-weight:700;font-size:21px;line-height:24px}
  .side-block span{display:block;font-size:20px;line-height:26px}
  .sb1{top:62px}.sb2{top:241px}
  .divider{position:absolute;left:18px;right:14px;top:182px;border-top:1.5px dashed #e9e4d9}
  .grid{left:340px;top:520px;width:848px;height:352px;border-bottom-right-radius:18px;overflow:hidden;background:var(--white)}
  .row{position:absolute;left:0;width:848px;font-weight:700;font-size:20px;color:#111}
  .row.shade{background:var(--row-grey)}
  .r1{top:0;height:91px}.r2{top:91px;height:90px}.r3{top:181px;height:81px}.r4{top:262px;height:90px}
  .cell{position:absolute;transform:translateX(-50%);white-space:nowrap}
  .c1{left:130px}.c2{left:423px}.c3{left:715px}
  .chev{position:absolute;width:60px;height:22px}
  .ch1{left:244px}.ch2{left:545px}
</style>
</head>
<body>
<div class="poster">
  <div class="abs brand">
    <div class="brand-mark"></div>
    <div class="brand-name">FIRST<br>BAPTIST<br>QUARRYDALE</div>
  </div>

  <div class="abs title-box">
    <h1 class="title">A READY CHURCH</h1>
    <div class="tagline">READY TO SERVE, READY TO LOVE, READY FOR WHEN JESUS RETURNS</div>
  </div>

  <div class="abs steeple-art" role="img" aria-label="Grey church steeple illustration"></div>

  <div class="abs pillar dark p1"><h2><span class="cap">P</span>RAYER</h2><p>Become a person devoted to prayer each day of your life</p></div>
  <div class="abs pillar tan p2"><h2><span class="cap">G</span>od's Word</h2><p>Build a daily habit of beholding God in His Word</p></div>
  <div class="abs pillar dark p3" style="padding-top:44px"><h2><span class="cap">B</span>iblical<br>Community</h2><p style="margin-top:2px">Engage deeply in Christian community</p></div>
  <div class="abs pointer pt1"></div>
  <div class="abs pointer pt2"></div>

  <div class="abs badge b1" role="img" aria-label="Praying hands icon"><span></span></div>
  <div class="abs badge b2" role="img" aria-label="Bible icon"><span></span></div>
  <div class="abs badge b3" role="img" aria-label="Joined hands icon"><span></span></div>

  <div class="abs habit dark" style="left:340px;width:263px">PRAY DAILY</div>
  <div class="abs habit tan" style="left:623px;width:281px">READ DAILY</div>
  <div class="abs habit dark" style="left:924px;width:264px">GATHER WEEKLY</div>

  <div class="abs start">START HERE
    <svg width="46" height="16" viewBox="0 0 46 16"><path d="M0 0h7l7 8-7 8H0l7-8z" fill="#fff"/><path d="M14 0h7l7 8-7 8h-7l7-8z" fill="#cfd1d2"/><path d="M28 0h7l7 8-7 8h-7l7-8z" fill="#7d8285"/></svg>
  </div>
  <div class="abs side">
    <div class="side-block sb1"><strong>FOCUSED. FAITHFUL.</strong><span>God's Work In Me</span></div>
    <div class="divider"></div>
    <div class="side-block sb2"><strong>PREPARED. LOOKING.</strong><span>God's Work Through Me</span></div>
  </div>

  <svg width="0" height="0" style="position:absolute">
    <defs>
      <g id="chevrons">
        <path d="M0 0h10l10 11-10 11H0l10-11z" fill="#373e41"/>
        <path d="M20 0h10l10 11-10 11H20l10-11z" fill="#6d7275"/>
        <path d="M40 0h10l10 11-10 11H40l10-11z" fill="#b9bbbc"/>
      </g>
    </defs>
  </svg>

  <div class="abs grid">
    <div class="row shade r1">
      <span class="cell c1" style="top:34px">REST</span>
      <svg class="chev ch1" style="top:40px" viewBox="0 0 60 22"><use href="#chevrons"/></svg>
      <span class="cell c2" style="top:34px">STUDY</span>
      <svg class="chev ch2" style="top:40px" viewBox="0 0 60 22"><use href="#chevrons"/></svg>
      <span class="cell c3" style="top:34px">CONNECT</span>
    </div>
    <div class="row r2">
      <span class="cell c1" style="top:33px">REFLECT</span>
      <svg class="chev ch1" style="top:36px" viewBox="0 0 60 22"><use href="#chevrons"/></svg>
      <span class="cell c2" style="top:33px">MEMORIZE</span>
      <svg class="chev ch2" style="top:36px" viewBox="0 0 60 22"><use href="#chevrons"/></svg>
      <span class="cell c3" style="top:33px;left:706px">LEARN</span>
    </div>
    <div class="row shade r3">
      <span class="cell c1" style="top:26px">FAST</span>
      <svg class="chev ch1" style="top:29px" viewBox="0 0 60 22"><use href="#chevrons"/></svg>
      <span class="cell c2" style="top:26px">TEACH</span>
      <svg class="chev ch2" style="top:29px" viewBox="0 0 60 22"><use href="#chevrons"/></svg>
      <span class="cell c3" style="top:26px;left:706px">SERVE</span>
    </div>
    <div class="row r4">
      <span class="cell c1" style="top:30px">INTERCEDE</span>
      <svg class="chev ch1" style="top:33px" viewBox="0 0 60 22"><use href="#chevrons"/></svg>
      <span class="cell c2" style="top:30px">PROCLAIM</span>
      <svg class="chev ch2" style="top:33px" viewBox="0 0 60 22"><use href="#chevrons"/></svg>
      <span class="cell c3" style="top:30px">GIVE</span>
    </div>
  </div>
</div>
</body>
</html>
```